Website redesign

We need a bold revamp of our website (http://www.brantwoodpower.co.nz/)
which at the moment looks dated. We want a crisp, fresh and bold look. The background image behind web page can go. Open to complete new layout

Target Market(s)

Electrical contracting company- working in the domestic and commercial field

Coding

Coded - Design and coding required

Number of Pages Required

5+ page

Font styles to use
Sans Serif

Colors

Designer to choose colors to be used in the design.

```html
<!DOCTYPE html>
<html lang="en">
<head>
<meta charset="utf-8">
<title>Brantwood Power</title>
<link rel="stylesheet" href="https://fonts.googleapis.com/css2?family=Play:wght@400;700&family=Open+Sans:wght@400;600;700&display=swap">
<style>
:root{
  --red:#f10000;
  --red-dark:#d40000;
  --ink:#1d1d1d;
  --text:#444;
  --muted:#777;
  --grey-bg:#f4f4f4;
  --tile:#f1f1f1;
  --white:#fff;
  --black:#111;
}
*{box-sizing:border-box;margin:0;padding:0}
html,body{width:1200px;height:3550px;overflow:hidden}
body{position:relative;background:var(--white);font-family:"Open Sans",Arial,sans-serif;color:var(--text)}
.abs{position:absolute}
.heading{font-family:"Play",Arial,sans-serif;color:var(--ink);text-align:center;left:0;width:1200px}
.sub{font-size:14px;color:var(--text);text-align:center;left:0;width:1200px}

/* header */
.brand{display:flex;align-items:center;gap:12px}
.brand-mark{width:30px;height:30px;background:var(--red)}
.brand-name{font-family:"Open Sans",Arial,sans-serif;font-weight:700;font-size:30px;line-height:1;color:var(--ink);letter-spacing:-.5px}
.contact-top{left:868px;top:30px;display:flex;gap:12px;align-items:center;font-size:14px;color:var(--ink);line-height:1.35}
.badge{left:1036px;top:28px;width:50px;height:50px;border-radius:50%;background:#39a6d8}
.nav{left:530px;top:92px;display:flex;gap:0;font-size:14px;font-weight:700;color:var(--ink)}
.nav a{color:inherit;text-decoration:none;padding:0 23px;position:relative}
.nav a.active{color:var(--red)}
.nav a.active::after{content:"";position:absolute;left:15px;right:15px;top:45px;height:6px;background:var(--red)}

/* hero */
.hero{left:0;top:147px;width:1200px;height:618px;background:linear-gradient(100deg,#d9e2ec 0%,#c3cfdc 45%,#9fb0c3 100%)}
.hero-title{left:130px;top:393px;font-family:"Play",Arial,sans-serif;font-weight:700;font-size:36px;color:var(--ink)}
.hero-title span{color:var(--red)}
.tiles{left:121px;top:717px;display:flex;gap:18px}
.tile{width:145px;height:143px;background:var(--tile);border-radius:4px;display:flex;flex-direction:column;align-items:center;justify-content:center;gap:14px;font-size:16px;color:var(--ink);box-shadow:0 2px 6px rgba(0,0,0,.08)}
.tile.active{background:var(--red);color:var(--white);font-weight:700}
.tile svg{width:52px;height:52px}
.round-arrow{width:22px;height:22px;border-radius:50%;border:2px solid var(--ink);display:flex;align-items:center;justify-content:center}
.round-arrow.red{border-color:var(--red)}

/* services */
.services{left:121px;top:1030px;display:flex;gap:8px}
.service{width:234px;text-align:center}
.service .photo{height:227px}
.service p{font-family:"Play",Arial,sans-serif;font-size:20px;letter-spacing:1px;color:var(--ink);margin-top:20px;line-height:1.25}
.btn{background:var(--red);color:var(--white);font-size:10px;font-weight:700;border-radius:14px;width:114px;height:28px;display:flex;align-items:center;justify-content:center;left:543px}

/* projects */
.projects-band{left:0;top:1453px;width:1200px;height:670px;background:var(--grey-bg)}

/* news */
.card{width:300px;height:326px;top:2294px;background:var(--white);box-shadow:0 2px 8px rgba(0,0,0,.08)}
.card .photo{height:190px;position:relative}
.date{position:absolute;left:0;top:0;width:34px;height:46px;background:var(--red);color:var(--white);font-size:12px;font-weight:700;text-align:center;line-height:1.1;padding-top:8px}
.date small{display:block;font-size:9px;font-weight:400}
.card h4{font-size:13px;font-weight:700;color:var(--red);margin:16px 0 0 4px}
.meta{display:flex;justify-content:space-between;font-size:12px;color:var(--text);margin:4px 4px 0}
.card .excerpt{font-size:13px;line-height:1.35;margin:10px 4px 0;color:var(--text)}
.card .more{font-size:13px;margin:8px 4px 0;color:var(--text)}

/* partners */
.partner{top:2805px;width:282px;height:130px;background:var(--white);box-shadow:0 1px 6px rgba(0,0,0,.12);display:flex;flex-direction:column;align-items:center;justify-content:center;gap:8px}
.partner .name{font-family:"Open Sans",Arial,sans-serif;font-weight:700;font-size:24px;color:var(--ink)}
.partner .tag{font-size:11px;font-weight:700;color:var(--ink);letter-spacing:.5px}

/* newsletter */
.signup{left:286px;top:3089px;width:578px;height:31px;background:var(--grey-bg);border-radius:16px;display:flex;align-items:center;font-size:12px;color:var(--text)}
.signup span{padding-left:26px;flex:1}
.signup b{width:123px;height:31px;background:var(--red);color:var(--white);border-radius:0 16px 16px 0;display:flex;align-items:center;justify-content:center;letter-spacing:2px;font-size:14px}

/* footer */
.footer{left:0;top:3186px;width:1200px;height:305px;background:var(--red);color:var(--white)}
.foot-logo{left:0;top:3252px;width:338px;height:102px;background:var(--white);display:flex;align-items:center;justify-content:center}
.foot-about{left:121px;top:3380px;width:230px;font-size:13px;font-weight:700;line-height:1.3;color:var(--white)}
.foot-h{font-size:13px;font-weight:700;color:var(--white);top:3249px}
.foot-h::after{content:"";display:block;width:36px;height:2px;background:var(--white);margin-top:6px}
.links{left:395px;top:3302px;list-style:none;font-size:13px;font-weight:700;line-height:26px;color:var(--white)}
.links li::before{content:"•";margin-right:10px}
.contacts{left:535px;top:3300px;font-size:13px;font-weight:700;line-height:26px;color:var(--white)}
.contacts div{display:flex;gap:10px;align-items:flex-start}
.contacts svg{width:14px;height:14px;margin-top:6px;flex:none}
.field{background:var(--red-dark);font-size:11px;color:var(--white);padding:7px 10px}
.send{left:933px;top:3418px;width:147px;height:29px;background:var(--black);color:var(--white);border-radius:15px;font-size:11px;font-weight:700;letter-spacing:1px;display:flex;align-items:center;justify-content:center}
.bottom-bar{left:0;top:3491px;width:1200px;height:59px;background:var(--black);color:var(--white);font-size:12px}
.social{left:884px;top:3507px;display:flex;gap:10px}
.social span{width:28px;height:28px;border-radius:50%;background:var(--white);display:flex;align-items:center;justify-content:center}
.social svg{width:14px;height:14px}
</style>
</head>
<body>

<!-- header -->
<div class="abs brand" style="left:118px;top:52px">
  <span class="brand-mark"></span>
  <span class="brand-name">Brantwood Power</span>
</div>
<div class="abs contact-top">
  <svg width="22" height="38" viewBox="0 0 22 38"><rect x="2" y="1" width="18" height="36" rx="3" fill="none" stroke="#1d1d1d" stroke-width="2"/><line x1="8" y1="32" x2="14" y2="32" stroke="#1d1d1d" stroke-width="2"/></svg>
  <div>0800 55 01 20<br>(06) 555 0144</div>
</div>
<div class="abs badge" aria-label="Accreditation badge" role="img"></div>
<nav class="abs nav">
  <a class="active">Home</a><a>About Us</a><a>Services</a><a>Projects</a><a>Contact Us</a><a>Info</a>
</nav>

<!-- hero -->
<div class="abs hero" role="img" aria-label="Photo of a security camera mounted on a pole against a soft blue sky"></div>
<div class="abs hero-title"><span>Security</span> Cameras</div>

<div class="abs round-arrow" style="left:86px;top:786px"><svg width="10" height="10" viewBox="0 0 10 10"><path d="M6.5 1.5L3 5l3.5 3.5" stroke="#1d1d1d" stroke-width="2" fill="none"/></svg></div>
<div class="abs round-arrow" style="left:1099px;top:786px"><svg width="10" height="10" viewBox="0 0 10 10"><path d="M3.5 1.5L7 5 3.5 8.5" stroke="#1d1d1d" stroke-width="2" fill="none"/></svg></div>

<div class="abs tiles">
  <div class="tile"><svg viewBox="0 0 52 52"><circle cx="26" cy="26" r="22" fill="none" stroke="#1d1d1d" stroke-width="3"/><path d="M29 10L17 29h9l-3 13 12-19h-9z" fill="#1d1d1d"/></svg>Electrical</div>
  <div class="tile active"><svg viewBox="0 0 52 52"><rect x="6" y="6" width="40" height="40" rx="3" fill="none" stroke="#fff" stroke-width="3"/><line x1="6" y1="16" x2="46" y2="16" stroke="#fff" stroke-width="3"/><rect x="13" y="22" width="26" height="17" fill="none" stroke="#fff" stroke-width="3"/><circle cx="13" cy="11" r="2" fill="#fff"/><circle cx="21" cy="11" r="2" fill="#fff"/><circle cx="29" cy="11" r="2" fill="#fff"/></svg>Appliances</div>
  <div class="tile"><svg viewBox="0 0 52 52"><path d="M14 36V24a12 12 0 0124 0v12l4 4H10z" fill="none" stroke="#1d1d1d" stroke-width="3" stroke-linejoin="round"/><path d="M22 44a4 4 0 008 0" fill="none" stroke="#1d1d1d" stroke-width="3"/><path d="M8 14a20 20 0 016-7M44 14a20 20 0 00-6-7" fill="none" stroke="#1d1d1d" stroke-width="3"/></svg>Alarms</div>
  <div class="tile"><svg viewBox="0 0 52 52"><path d="M26 4l18 7v13c0 12-8 20-18 24C16 44 8 36 8 24V11z" fill="none" stroke="#1d1d1d" stroke-width="3"/><rect x="19" y="24" width="14" height="11" fill="#1d1d1d"/><path d="M21 24v-4a5 5 0 0110 0v4" fill="none" stroke="#1d1d1d" stroke-width="3"/></svg>Security</div>
  <div class="tile"><svg viewBox="0 0 52 52"><circle cx="26" cy="26" r="21" fill="none" stroke="#1d1d1d" stroke-width="3"/><path d="M15 20c4-4 8 4 12 0s8 4 12 0M15 28c4-4 8 4 12 0s8 4 12 0M15 36c4-4 8 4 12 0s8 4 12 0" fill="none" stroke="#1d1d1d" stroke-width="3"/></svg>Heat Pumps</div>
  <div class="tile"><svg viewBox="0 0 52 52"><path d="M26 4c2 10 14 16 14 28a14 14 0 01-28 0c0-7 4-11 6-14 0 5 3 8 5 8-1-8 1-15 3-22z" fill="none" stroke="#1d1d1d" stroke-width="3" stroke-linejoin="round"/></svg>Fire / Smoke</div>
</div>

<!-- services -->
<h2 class="abs heading" style="top:943px;font-size:24px;font-weight:400;letter-spacing:1px">Our Services</h2>
<p class="abs sub" style="top:973px">Lorem Ipsum is simply dummy and typesetting industry</p>
<div class="abs round-arrow" style="left:1026px;top:946px;width:20px;height:20px"><svg width="9" height="9" viewBox="0 0 10 10"><path d="M6.5 1.5L3 5l3.5 3.5" stroke="#1d1d1d" stroke-width="2" fill="none"/></svg></div>
<div class="abs round-arrow red" style="left:1056px;top:946px;width:20px;height:20px"><svg width="9" height="9" viewBox="0 0 10 10"><path d="M3.5 1.5L7 5 3.5 8.5" stroke="#f10000" stroke-width="2" fill="none"/></svg></div>

<div class="abs services">
  <div class="service"><div class="photo" role="img" aria-label="Photo of a residential interior with downlights" style="background:linear-gradient(160deg,#c9a27a,#8a6a4c)"></div><p>Residential<br>Electrical</p></div>
  <div class="service"><div class="photo" role="img" aria-label="Photo of commercial conduit runs on a ceiling" style="background:linear-gradient(160deg,#d8d8d6,#9a9a98)"></div><p>Commercial<br>Electrical</p></div>
  <div class="service"><div class="photo" role="img" aria-label="Photo of a wall-mounted heat pump unit" style="background:linear-gradient(160deg,#b98b58,#ece9e4 55%)"></div><p style="margin-top:24px">Kaiora Heat<br>Pumps</p></div>
  <div class="service"><div class="photo" role="img" aria-label="Photo of a ceiling smoke alarm" style="background:linear-gradient(160deg,#e7e1dc,#c7bcb4)"></div><p style="margin-top:34px">Fire Alarms</p></div>
</div>
<div class="abs btn" style="top:1364px">View More</div>

<!-- projects -->
<div class="abs projects-band"></div>
<h2 class="abs heading" style="top:1495px;font-size:23px;font-weight:400;letter-spacing:1px">Projects Gallery</h2>
<p class="abs sub" style="top:1526px">Lorem Ipsum is simply dummy and typesetting industry</p>
<div class="abs" role="img" aria-label="Photo of an electrician testing a switchboard" style="left:121px;top:1590px;width:312px;height:185px;background:linear-gradient(135deg,#cfd3d8,#8c97a3)"></div>
<div class="abs" role="img" aria-label="Photo of a modern kitchen with appliances" style="left:445px;top:1590px;width:310px;height:202px;background:linear-gradient(135deg,#eceae6,#7b7b7b)"></div>
<div class="abs" role="img" aria-label="Photo of an outdoor heat pump unit" style="left:767px;top:1590px;width:313px;height:185px;background:linear-gradient(135deg,#5b4a3c,#cfcfcf)"></div>
<div class="abs" role="img" aria-label="Photo of a security monitoring room with screens" style="left:121px;top:1789px;width:312px;height:218px;background:linear-gradient(135deg,#3c5f82,#9fb4c8)"></div>
<div class="abs brand" style="left:470px;top:1880px;gap:10px">
  <span class="brand-mark" style="width:24px;height:24px"></span>
  <span class="brand-name" style="font-size:26px">Brantwood Power</span>
</div>
<div class="abs" role="img" aria-label="Photo of a technician installing an antenna on a roof" style="left:767px;top:1789px;width:313px;height:218px;background:linear-gradient(160deg,#6b8fbf,#2f4e77)"></div>
<div class="abs btn" style="top:2045px">View More</div>

<!-- news -->
<h2 class="abs heading" style="top:2208px;font-size:24px;font-weight:700">NEWS</h2>
<p class="abs sub" style="top:2239px">Lorem Ipsum is simply dummy text.</p>
<div class="abs round-arrow" style="left:1026px;top:2216px;width:20px;height:20px"><svg width="9" height="9" viewBox="0 0 10 10"><path d="M6.5 1.5L3 5l3.5 3.5" stroke="#1d1d1d" stroke-width="2" fill="none"/></svg></div>
<div class="abs round-arrow red" style="left:1056px;top:2216px;width:20px;height:20px"><svg width="9" height="9" viewBox="0 0 10 10"><path d="M3.5 1.5L7 5 3.5 8.5" stroke="#f10000" stroke-width="2" fill="none"/></svg></div>

<article class="abs card" style="left:121px">
  <div class="photo" role="img" aria-label="Photo of a kitchen with pendant lights" style="background:linear-gradient(135deg,#8a8a8a,#3d3d3d)"><div class="date">01<small>Feb</small></div></div>
  <h4>POST TITLE</h4>
  <div class="meta"><span>▦ February 26, 2018</span><span>💬 20 &nbsp; ♡ 12</span></div>
  <p class="excerpt">Lorem Ipsum is simply dummy text of the And printing matter and typesetting industry.</p>
  <p class="more">Read More.. ›</p>
</article>
<article class="abs card" style="left:451px">
  <div class="photo" role="img" aria-label="Photo of an electrician working in a timber roof frame" style="background:linear-gradient(135deg,#b88a5c,#5a3e27)"><div class="date">10<small>Feb</small></div></div>
  <h4>POST TITLE</h4>
  <div class="meta"><span>▦ February 26, 2018</span><span>💬 20 &nbsp; ♡ 12</span></div>
  <p class="excerpt">Lorem Ipsum is simply dummy text of the printing and typesetting industry.</p>
  <p class="more">Read More.. ›</p>
</article>
<article class="abs card" style="left:780px">
  <div class="photo" role="img" aria-label="Photo of an electrician wiring a switchboard" style="background:linear-gradient(135deg,#e8ecef,#4d8bc6)"><div class="date">22<small>Feb</small></div></div>
  <h4>POST TITLE</h4>
  <div class="meta"><span>▦ February 22, 2018</span><span>💬 20 &nbsp; ♡ 12</span></div>
  <p class="excerpt">Lorem Ipsum is simply dummy text of the printing and typesetting industry.</p>
  <p class="more">Read More.. ›</p>
</article>
<div class="abs btn" style="top:2672px">View More</div>

<!-- partners -->
<h2 class="abs heading" style="top:2742px;font-size:24px;font-weight:700;letter-spacing:1px">WE ARE AUTHORISED INSTALLERS FOR</h2>
<div class="abs partner" style="left:305px"><span class="name">Kaiora Heat Pumps</span><span class="tag">COMFORT ALL YEAR ROUND</span></div>
<div class="abs partner" style="left:611px"><span class="name">Heatwise Group</span><span class="tag">HEAT PUMP SPECIALISTS</span></div>

<!-- newsletter -->
<h2 class="abs heading" style="top:3010px;font-size:20px;font-weight:700;letter-spacing:1px">SUBSCRIBE TO OUR NEWSLETTER</h2>
<p class="abs sub" style="top:3038px;font-size:15px;letter-spacing:.5px;color:var(--ink)">to receive the latest news &amp; update</p>
<div class="abs signup"><span>Your Email</span><b>SUBMIT</b></div>

<!-- footer -->
<footer class="abs footer"></footer>
<div class="abs foot-logo">
  <div class="brand" style="gap:10px"><span class="brand-mark" style="width:24px;height:24px"></span><span class="brand-name" style="font-size:24px">Brantwood Power</span></div>
</div>
<p class="abs foot-about">Lorem Ipsum is simply dummy text of the printing and typesetting Lorem Ipsum Industry.</p>

<div class="abs foot-h" style="left:395px">QUICK LINK</div>
<ul class="abs links"><li>Home</li><li>About Us</li><li>Services</li><li>Projects</li><li>Contact Us</li><li>Info</li></ul>

<div class="abs foot-h" style="left:535px">CONTACT US</div>
<div class="abs contacts">
  <div><svg viewBox="0 0 14 14"><path d="M7 1a4.5 4.5 0 00-4.5 4.5C2.5 9 7 13 7 13s4.5-4 4.5-7.5A4.5 4.5 0 007 1z" fill="#fff"/><circle cx="7" cy="5.5" r="1.6" fill="#f10000"/></svg><span>: &nbsp;14 Kereru Lane,<br>&nbsp;&nbsp;&nbsp;Riverton 4510</span></div>
  <div><svg viewBox="0 0 14 14"><path d="M3 1l2.5 3-1.5 1.5c1 2 2.5 3.5 4.5 4.5L10 8.5l3 2.5-1.5 2C6 13 1 8 1 2.5z" fill="#fff"/></svg><span>: &nbsp;0800 55 01 20</span></div>
  <div><svg viewBox="0 0 14 14"><path d="M3 1l2.5 3-1.5 1.5c1 2 2.5 3.5 4.5 4.5L10 8.5l3 2.5-1.5 2C6 13 1 8 1 2.5z" fill="#fff"/></svg><span>: &nbsp;(06) 555 0144</span></div>
  <div><svg viewBox="0 0 14 14"><rect x="3" y="1" width="8" height="4" fill="#fff"/><rect x="1" y="5" width="12" height="6" fill="#fff"/><rect x="3" y="9" width="8" height="4" fill="#fff" stroke="#f10000"/></svg><span>: &nbsp;(06) 555 0188</span></div>
  <div><svg viewBox="0 0 14 14"><rect x="1" y="3" width="12" height="8" fill="#fff"/><path d="M1 3l6 5 6-5" fill="none" stroke="#f10000"/></svg><span>: &nbsp;office@brantwoodpower.co.nz</span></div>
</div>

<div class="abs foot-h" style="left:805px">QUICK CONTACT</div>
<div class="abs field" style="left:805px;top:3309px;width:135px;height:26px">Name</div>
<div class="abs field" style="left:945px;top:3309px;width:135px;height:26px">Phone</div>
<div class="abs field" style="left:805px;top:3340px;width:275px;height:64px">Message</div>
<div class="abs send">SEND</div>

<div class="abs bottom-bar"><span class="abs" style="left:121px;top:22px">Copyright 2018 Brantwood Power. All Rights Reserved.</span></div>
<div class="abs social" aria-label="Social links">
  <span><svg viewBox="0 0 14 14"><circle cx="3" cy="7" r="2" fill="#111"/><circle cx="11" cy="3" r="2" fill="#111"/><circle cx="11" cy="11" r="2" fill="#111"/><path d="M3 7l8-4M3 7l8 4" stroke="#111" stroke-width="1.3"/></svg></span>
  <span><svg viewBox="0 0 14 14"><rect x="1" y="3" width="12" height="8" fill="none" stroke="#111" stroke-width="1.5"/><path d="M1 3l6 5 6-5" fill="none" stroke="#111" stroke-width="1.5"/></svg></span>
  <span><svg viewBox="0 0 14 14"><path d="M2 2h10v7H6l-3 3V9H2z" fill="#111"/></svg></span>
  <span><svg viewBox="0 0 14 14"><circle cx="7" cy="7" r="5.5" fill="none" stroke="#111" stroke-width="1.4"/><path d="M1.5 7h11M7 1.5c-3 3.5-3 7.5 0 11M7 1.5c3 3.5 3 7.5 0 11" fill="none" stroke="#111" stroke-width="1.1"/></svg></span>
  <span><svg viewBox="0 0 14 14"><path d="M7 12s-5-3-5-6.5A2.6 2.6 0 017 4a2.6 2.6 0 015 1.5C12 9 7 12 7 12z" fill="#111"/></svg></span>
</div>

</body>
</html>
```